Forex Trading Software Sales Page

We need header, footer, mid section and background design for our new website for a forex software that helps people make better decision in forex trading. Simple Sales Page. You can use test name "Meridel Sample Layout" on the design itself.

The new design must be blue tone, corporate, look expensive, show confidence and wealth. Please show us how you can improve our current design style by making something similar to the designed attached or making something entirely different that will better deliver the message to the visitors.

3 Examples of our previous designs are attached.

Target Market(s)

Forex Beginners, People who want to make money at home.

Industry/Entity Type

Business

Number of Pages Required

1 page

Font styles to use
Sans Serif

Colors
0255a3
eaf1f7
ffffff

Requirements
Must have
• The design must be 90% similar to this:
• https://www.quarnelbay7.com/
• 1) Name "Meridel Sample Layout" on header and footer.
• 2) PSDs of header, footer, mid section and background design.
• 3) Images of money bags, stacks etc
• 4) Show wealth, confidence and look expensive
• 5) Blueish tone of website mainly
• 6) Sample of headline and content colors and fonts.
Nice to have
• People will be buying products from this website, so it must not look too cheesy or over promising. Must give confidence and look expensive and clean.
Should not have
• Images of cars, yachts, villas or anything else that is associated with being rich.

```html
<!DOCTYPE html>
<html lang="en">
<head>
<meta charset="utf-8">
<title>Meridel Sample Layout</title>
<link href="https://fonts.googleapis.com/css2?family=Bowlby+One+SC&family=Roboto:ital,wght@0,400;0,500;0,700;1,700&family=Russo+One&display=swap" rel="stylesheet">
<style>
:root{
  --brand:#0255a3;
  --brand-dark:#013a73;
  --navy:#071b3d;
  --navy-2:#0c2c5c;
  --ice:#eaf1f7;
  --white:#ffffff;
  --cyan:#5fd3f3;
  --grey:#d6dce3;
  --ink:#1d2733;
  --gold:#ffe14a;
}
*{box-sizing:border-box;margin:0;padding:0}
html,body{width:1200px;height:4580px;overflow:hidden}
body{font-family:"Roboto",Arial,sans-serif;color:var(--ink);position:relative;background:var(--navy)}
.backdrop{position:absolute;inset:0;background:linear-gradient(90deg,#0a2347 0%,#1b4f7a 6%,#6b5a2a 9%,#0a2347 11.4%,#0a2347 88.6%,#6b5a2a 91%,#1b4f7a 94%,#0a2347 100%)}
.column{position:absolute;left:140px;top:0;width:920px;height:4580px;background:var(--grey);overflow:hidden}
.section{position:absolute;left:0;width:920px}
.center{text-align:center}
.display{font-family:"Bowlby One SC","Russo One",sans-serif;color:var(--cyan);letter-spacing:2px}
.btn{display:inline-block;font:500 13px "Roboto",sans-serif;color:var(--white);background:var(--brand);padding:8px 18px;border-radius:4px;text-transform:uppercase}
.btn-ghost{background:transparent;border:2px solid var(--white);border-radius:20px}
.arrow{position:absolute;width:34px;height:34px;border-radius:50%;background:rgba(255,255,255,.85)}
.arrow svg{display:block;margin:9px}
/* header */
.nav{top:0;height:60px;background:rgba(2,40,90,.92);z-index:2;display:flex;align-items:center;justify-content:space-between;padding:0 50px 0 60px}
.logo{display:flex;align-items:center;gap:10px;color:var(--white);font:500 20px "Roboto",sans-serif}
.logo-mark{width:22px;height:22px;background:var(--white)}
.nav-links{display:flex;gap:34px;list-style:none;font:500 13px "Roboto",sans-serif;color:var(--white)}
.nav-links .active{color:var(--cyan)}
.hero{top:0;height:427px;background:radial-gradient(ellipse at 50% 45%,#2f6fa8 0%,#123e72 55%,#071b3d 100%);color:var(--white)}
.hero-title{position:absolute;top:135px;width:100%;font:400 52px/1.1 "Russo One",sans-serif;color:var(--white);letter-spacing:2px;white-space:nowrap}
.hero-sub{position:absolute;top:240px;width:100%;font:700 26px "Roboto",sans-serif;color:#c9f3ff;line-height:1.35}
.hero-tag{position:absolute;top:335px;width:100%;font:700 26px "Roboto",sans-serif;color:#c9f3ff}
/* about */
.about{top:473px;height:412px;background:linear-gradient(100deg,#0b2a55 0%,#1c4f86 45%,#6d8fb4 100%);color:var(--white);padding:30px 60px}
.about h2{font-size:50px}
.about p{margin-top:20px;width:560px;font-size:14px;line-height:1.5;color:#dbe8f5}
.about .btn{position:absolute;left:400px;top:300px}
/* video */
.video{top:891px;height:360px;background:linear-gradient(90deg,#141a24 0%,#1e2633 40%,#0c1b33 100%)}
.claim{top:1267px;font:500 25px "Roboto",sans-serif;color:var(--ink)}
.claim em{display:block;margin-top:6px;font:italic 700 22px "Roboto",sans-serif;color:var(--cyan);text-shadow:1px 1px 0 #1a3050}
.claim u{color:var(--brand)}
/* services */
.services{top:1435px;height:427px;background:linear-gradient(180deg,#0b1f45,#0d3770);color:var(--white)}
.services h2{position:absolute;top:22px;width:100%;font-size:50px}
.card{position:absolute;top:95px;width:250px;height:205px;border:2px solid var(--white);background:rgba(40,80,130,.55);text-align:center;padding-top:22px}
.card .ico{width:34px;height:34px;margin:0 auto 10px}
.card h3{font:500 18px "Roboto",sans-serif}
.card p{font-size:12px;margin:10px 28px 16px;line-height:1.4}
.card .btn{font-size:11px;padding:6px 14px}
.services .more{position:absolute;left:390px;top:375px;font-size:11px}
/* help */
.help{top:1917px;height:153px;background:linear-gradient(90deg,#28476e,#6c8aa9 60%,#3a5a80)}
.help h2{position:absolute;top:28px;width:100%;font:500 24px "Roboto",sans-serif;color:var(--white)}
.search{position:absolute;top:70px;left:160px;width:520px;height:40px;background:var(--ice);font:500 17px "Roboto",sans-serif;letter-spacing:3px;color:#5a7592;padding:10px 14px;text-align:left}
.search-btn{position:absolute;top:70px;left:690px;width:70px;height:40px;background:var(--brand);border-radius:3px}
.search-btn svg{display:block;margin:8px auto}
/* faq */
.faq{top:2076px;height:595px}
.faq h2{position:absolute;top:20px;width:100%;font-size:50px}
.faq-card{position:absolute;top:88px;left:60px;width:800px;height:500px;background:var(--white);border-radius:6px;padding:26px 30px}
.faq-row{display:flex;align-items:center;gap:16px;height:41.5px;font-size:15px}
.faq-row b{flex:none;width:28px;height:28px;border-radius:50%;background:var(--brand);color:var(--white);font:700 14px/28px "Roboto",sans-serif;text-align:center}
.faq-row.answer span{color:var(--brand)}
.faq .btn{position:absolute;left:350px;bottom:14px;border-radius:16px;font-size:12px}
/* contact */
.contact{top:2732px;height:565px;background:linear-gradient(135deg,#5d6b4f 0%,#9aa387 40%,#4e5c47 100%)}
.board{position:absolute;left:110px;top:13px;width:700px;height:545px;background:var(--white)}
.board h2{position:absolute;top:22px;width:100%;font-size:44px}
.field{position:absolute;border:2px solid var(--brand);font:500 16px "Roboto",sans-serif;letter-spacing:2px;color:#8a99a8;padding:11px 14px}
.send{position:absolute;left:255px;top:450px;width:185px;height:46px;border:2px solid var(--brand);font:500 17px/42px "Roboto",sans-serif;letter-spacing:3px;color:var(--brand);text-align:center}
/* order */
.order{top:3358px;height:473px;background:var(--white)}
.product{position:absolute;left:80px;top:60px;width:300px;height:360px;background:linear-gradient(160deg,#0a2f66,#2a6db0 55%,#5a7a3a)}
.order h2{position:absolute;left:475px;top:40px;font:400 40px "Russo One",sans-serif;color:var(--cyan)}
.offer-label{position:absolute;left:475px;top:100px;font:500 22px "Roboto",sans-serif;color:#111}
.price{position:absolute;left:475px;width:325px;height:56px;text-align:center;font:500 22px/56px "Roboto",sans-serif}
.price.regular{top:132px;background:var(--brand);color:#cfe2f5;text-decoration:line-through}
.price.deal{top:200px;background:#000;color:var(--gold);border:2px solid var(--brand);font-weight:700;line-height:52px}
.buy{position:absolute;left:535px;top:290px;width:205px;height:62px;background:var(--brand);border-radius:8px;color:var(--white);font:500 32px/62px "Roboto",sans-serif;text-align:center}
.pay{position:absolute;top:380px;width:68px;height:42px;border-radius:4px;background:var(--ice);border:1px solid #b9c8d8}
/* newsletter */
.newsletter{top:3902px;height:128px;background:linear-gradient(90deg,#2f4f78,#7892b0 55%,#3a5a84)}
.newsletter h2{position:absolute;top:20px;width:100%;font:700 18px "Roboto",sans-serif;color:#d8ecff;letter-spacing:1px;text-transform:uppercase}
.nl-input{position:absolute;left:195px;top:58px;width:400px;height:36px;background:#dfe8f1;font:700 13px/36px "Roboto",sans-serif;color:#7a90a8;padding-left:14px;letter-spacing:1px;text-transform:uppercase}
.nl-send{position:absolute;left:605px;top:58px;width:115px;height:36px;border-radius:18px;background:var(--brand);color:var(--white);font:500 16px/36px "Roboto",sans-serif;text-align:center}
/* partners */
.partners{top:4106px;height:184px;background:var(--brand);color:var(--white)}
.partners h2{position:absolute;top:24px;width:100%;font:500 24px "Roboto",sans-serif;letter-spacing:4px}
.badge{position:absolute;top:80px;width:190px;height:64px;border-radius:10px;background:#e9eef4}
/* footer */
.footer{top:4320px;height:260px;background:var(--navy-2);color:var(--white)}
.footer .logo{position:absolute;left:60px;top:30px;font-size:17px}
.follow{position:absolute;left:370px;top:28px;font-size:16px}
.social{display:flex;gap:8px;margin-top:10px}
.social i{width:22px;height:22px;background:var(--white);border-radius:3px}
.foot-links{position:absolute;left:615px;top:26px;list-style:none;font:500 21px/30px "Roboto",sans-serif;letter-spacing:1px}
.foot-links li::before,.legal span::before{content:"";display:inline-block;width:8px;height:8px;background:var(--white);transform:rotate(45deg);margin-right:14px;vertical-align:middle}
.legal{position:absolute;left:60px;top:128px;display:flex;gap:30px;font-size:16px}
.copyright{position:absolute;left:0;bottom:0;width:100%;height:31px;background:var(--brand-dark);font-size:14px;line-height:31px;text-align:center}
</style>
</head>
<body>
<div class="backdrop" role="img" aria-label="Dark blue wallpaper of banknotes, money stacks and gold dollar signs"></div>
<main class="column">

  <header class="section hero center" role="img" aria-label="Blue city skyline with glowing trading light effects">
    <div class="hero-title">MERIDEL SAMPLE LAYOUT</div>
    <div class="hero-sub">New Trading Secret That is Able To Accurately Predict a<br>New Trend Before It Even Starts!</div>
    <div class="hero-tag">And generate a fast buy or sell signal!</div>
    <span class="arrow" style="left:12px;top:196px"><svg width="16" height="16" viewBox="0 0 16 16"><path d="M11 2 5 8l6 6" fill="none" stroke="#0255a3" stroke-width="3"/></svg></span>
    <span class="arrow" style="right:12px;top:196px"><svg width="16" height="16" viewBox="0 0 16 16"><path d="m5 2 6 6-6 6" fill="none" stroke="#0255a3" stroke-width="3"/></svg></span>
  </header>

  <nav class="section nav">
    <div class="logo"><span class="logo-mark"></span>Meridel Sample Layout</div>
    <ul class="nav-links"><li>HOME</li><li class="active">ABOUT US</li><li>OUR SERVICE</li><li>FAQ</li><li>CONTACT US</li><li>ORDER NOW</li></ul>
  </nav>

  <section class="section about" role="img" aria-label="Business team in a meeting, blue tinted">
    <h2 class="display">ABOUT US</h2>
    <p>Pivot Compass Pro is a trend tool carefully designed for reading market flow and spotting strong price movements.<br>It studies many currency pairs and time frames, then shows a clear buy or sell signal so you can act with calm and a steady plan.</p>
    <p>Trading should not be guesswork. When a signal appears on your chart you can be confident that the move is backed by clear rules, so you can trade with less stress and more control.</p>
    <span class="btn btn-ghost">Read more</span>
  </section>

  <section class="section video" role="img" aria-label="Trading platform screenshot with price table and candlestick chart, with a play button"></section>

  <p class="section claim center">We know that most traders lose more than they make in Forex...
    <em>But this video will show you everything about us and our working<br>principles and it will also show you how to get most profit with <u>Meridel Sample Layout.</u></em></p>

  <section class="section services center">
    <h2 class="display">SERVICES</h2>
    <div class="card" style="left:58px">
      <svg class="ico" viewBox="0 0 34 34"><path d="M6 20v-4a11 11 0 0 1 22 0v4" fill="none" stroke="#fff" stroke-width="3"/><rect x="4" y="18" width="6" height="10" rx="2" fill="#fff"/><rect x="24" y="18" width="6" height="10" rx="2" fill="#fff"/></svg>
      <h3>24/7<br>Support</h3><p>We Provide 24/7 Support to all our customers</p><span class="btn">Read more</span>
    </div>
    <div class="card" style="left:333px">
      <svg class="ico" viewBox="0 0 34 34"><circle cx="17" cy="17" r="14" fill="none" stroke="#fff" stroke-width="3"/><path d="M10 17h14M17 10v14" stroke="#fff" stroke-width="3"/></svg>
      <h3>FREEDOM</h3><p>With this powerful tool enjoy a complete financial freedom</p><span class="btn">Read more</span>
    </div>
    <div class="card" style="left:608px">
      <svg class="ico" viewBox="0 0 34 34"><path d="M9 24V15a8 8 0 0 1 16 0v9l3 3H6z" fill="#fff"/><circle cx="17" cy="30" r="3" fill="#fff"/></svg>
      <h3>ALERTS</h3><p>Get alerts with our emailing service or directly to your mobile</p><span class="btn">Read more</span>
    </div>
    <span class="btn more">See more services</span>
  </section>

  <section class="section help center" role="img" aria-label="Support agents with headsets, blue tinted">
    <h2>HI, HOW CAN WE HELP YOU?</h2>
    <div class="search">SEARCH</div>
    <div class="search-btn"><svg width="24" height="24" viewBox="0 0 24 24"><circle cx="10" cy="10" r="7" fill="none" stroke="#fff" stroke-width="3"/><path d="m15 15 6 6" stroke="#fff" stroke-width="3"/></svg></div>
  </section>

  <section class="section faq">
    <h2 class="display center">FAQ'S</h2>
    <div class="faq-card">
      <div class="faq-row"><b>Q</b><span>This website looks familiar to me.. Is it the same software that I already purchased from you?</span></div>
      <div class="faq-row answer"><b>A</b><span>No. It is a brand new website/product... It is not similar in any way to any of my other products.</span></div>
      <div class="faq-row"><b>Q</b><span>What do I need to start trading with Pivot Compass Pro?</span></div>
      <div class="faq-row answer"><b>A</b><span>You need a computer with an internet connection and TX4 terminal</span></div>
      <div class="faq-row"><b>Q</b><span>Time frames?</span></div>
      <div class="faq-row answer"><b>A</b><span>The "Pivot Compass Pro" is designed to work on M15, M30, H1, H4 and D1 timeframes.</span></div>
      <div class="faq-row"><b>Q</b><span>What do I need to start trading with Pivot Compass Pro?</span></div>
      <div class="faq-row answer"><b>A</b><span>You need a computer with an internet connection and TX4 terminal</span></div>
      <div class="faq-row"><b>Q</b><span>Time frames?</span></div>
      <div class="faq-row answer"><b>A</b><span>The "Pivot Compass Pro" is designed to work on M15, M30, H1, H4 and D1 timeframes.</span></div>
      <span class="btn">Load more</span>
    </div>
  </section>

  <section class="section contact" role="img" aria-label="Banknotes background with hands holding a white board">
    <div class="board">
      <h2 class="display center">CONTACT US</h2>
      <div class="field" style="left:140px;top:80px;width:180px;height:46px">FIRST NAME</div>
      <div class="field" style="left:370px;top:80px;width:180px;height:46px">LAST NAME</div>
      <div class="field" style="left:140px;top:160px;width:410px;height:46px">ENTER YOUR EMAIL</div>
      <div class="field" style="left:140px;top:235px;width:410px;height:175px">TYPE YOUR MESSAGE</div>
      <div class="send">SEND</div>
    </div>
  </section>

  <section class="section order">
    <div class="product" role="img" aria-label="Pivot Compass Pro software box with money stacks"></div>
    <h2>ORDER NOW</h2>
    <div class="offer-label">SPECIAL OFFER</div>
    <div class="price regular">Regular Price $147</div>
    <div class="price deal">Offer Price $87</div>
    <div class="buy">BUY NOW</div>
    <span class="pay" style="left:485px"></span><span class="pay" style="left:560px"></span><span class="pay" style="left:635px"></span><span class="pay" style="left:710px"></span><span class="pay" style="left:785px"></span>
    <span class="arrow" style="left:0;top:215px;border-radius:0;background:#6b93bd"><svg width="16" height="16" viewBox="0 0 16 16"><path d="M11 2 5 8l6 6" fill="none" stroke="#fff" stroke-width="3"/></svg></span>
    <span class="arrow" style="right:0;top:215px;border-radius:0;background:#6b93bd"><svg width="16" height="16" viewBox="0 0 16 16"><path d="m5 2 6 6-6 6" fill="none" stroke="#fff" stroke-width="3"/></svg></span>
  </section>

  <section class="section newsletter center" role="img" aria-label="Blue tinted office background">
    <h2>Sign up for our daily newsletter</h2>
    <div class="nl-input">Enter your email address</div>
    <div class="nl-send">Send</div>
  </section>

  <section class="section partners center">
    <h2>TRUSTED PARTNERS</h2>
    <span class="badge" style="left:115px"></span><span class="badge" style="left:365px"></span><span class="badge" style="left:615px"></span>
    <span class="arrow" style="left:14px;top:95px;background:transparent"><svg width="16" height="16" viewBox="0 0 16 16"><path d="M11 2 5 8l6 6" fill="none" stroke="#fff" stroke-width="3"/></svg></span>
    <span class="arrow" style="right:14px;top:95px;background:transparent"><svg width="16" height="16" viewBox="0 0 16 16"><path d="m5 2 6 6-6 6" fill="none" stroke="#fff" stroke-width="3"/></svg></span>
  </section>

  <footer class="section footer">
    <div class="logo"><span class="logo-mark"></span>Meridel Sample Layout</div>
    <div class="follow">Follow Us<div class="social"><i></i><i></i><i></i></div></div>
    <div class="legal"><span>Disclaimer</span><span>Affiliates</span></div>
    <ul class="foot-links"><li>Home</li><li>About us</li><li>Our Service</li><li>FAQ</li><li>Contact Us</li><li>Order Now</li></ul>
    <div class="copyright">© Copyright-2017 Meridel Sample Layout All rights reserved</div>
  </footer>

</main>
</body>
</html>
```